TRL Vetting Background Check Company

TRL Vetting is an eCommerce background check company offering three services payable online. The Candidate Review Unit is a team of skilled, experienced investigators who regularly conduct fact-findings (many daily) on federal, state, and local background checks.

Target Market(s)

All businesses that hire employees, as well as domestic persons that have a need for nannies, housekeepers and handymen. Persons in the dating community will utilize the services also.

Coding

Coded - Design and coding required

Font styles to use
Sans Serif

```html
<!DOCTYPE html>
<html lang="en">
<head>
<meta charset="utf-8">
<title>TRL Vetting – Background Checks</title>
<link href="https://fonts.googleapis.com/css2?family=Noto+Sans:wght@400;600;700&family=Open+Sans:wght@400;600;700&family=Libre+Baskerville&display=swap" rel="stylesheet">
<style>
:root{
  --navy:#13225f;
  --navy-deep:#0d1530;
  --red:#c21d2e;
  --text:#6b6f7b;
  --ink:#1d2233;
  --light:#f3f6fb;
  --grey:#efefef;
  --white:#fff;
}
*{margin:0;padding:0;box-sizing:border-box}
html,body{width:1200px;height:4298px;overflow:hidden}
body{position:relative;font-family:"Open Sans",sans-serif;color:var(--ink);background:var(--white)}
.abs{position:absolute}
.heading{font-family:"Noto Sans",sans-serif;font-weight:700;color:var(--navy)}
.label{font-size:12px;color:var(--red);text-transform:uppercase;text-decoration:underline;text-underline-offset:4px}

/* header */
.site-header{left:0;top:0;width:1200px;height:144px;background:var(--light)}
.brand{left:112px;top:36px;display:flex;align-items:center;gap:10px}
.brand-mark{width:34px;height:34px;border-radius:50%;background:var(--red)}
.brand-name{font-family:"Noto Sans",sans-serif;font-weight:700;font-size:26px;color:var(--navy)}
.contact-item{top:34px;display:flex;gap:12px;font-family:Arial,sans-serif;font-size:13px;color:#555;line-height:19px}
.contact-item svg{margin-top:4px}
.nav{left:244px;top:113px;width:881px;height:49px;background:var(--white);border-radius:24px 0 0 24px;box-shadow:0 3px 8px rgba(0,0,0,.12)}
.nav a{position:absolute;top:15px;font-family:Arial,sans-serif;font-size:13px;color:#333;text-decoration:none}
.btn-appoint{left:966px;top:113px;width:157px;height:47px;border-radius:24px;background:var(--red);color:#fff;font-family:Arial,sans-serif;font-size:14px;display:flex;align-items:center;justify-content:center;box-shadow:0 3px 6px rgba(0,0,0,.2)}

/* hero */
.hero-photo{left:0;top:144px;width:1200px;height:906px;background:linear-gradient(100deg,#13235c 0%,#1d3270 40%,#5a6f96 70%,#9aa7bd 100%)}
.hero-box{left:92px;top:345px;width:531px;height:298px;background:rgba(40,55,100,.55)}
.hero-bar{left:90px;top:387px;width:4px;height:80px;background:var(--red)}
.hero-title{left:118px;top:376px;font-family:"Noto Sans",sans-serif;font-weight:600;font-size:37px;line-height:50px;color:#fff;letter-spacing:.5px}
.hero-text{left:120px;top:490px;width:500px;font-size:14px;line-height:29px;color:#fff}
.btn-red{background:var(--red);color:#fff;font-weight:700;font-size:14px;display:flex;align-items:center;justify-content:center;gap:10px}

/* about */
.about-text p{font-size:12px;line-height:19px;color:var(--text)}

/* services */
.services{left:0;top:1432px;width:1200px;height:663px;background:var(--grey)}
.card-photo{width:304px;height:280px}
.card-body{width:237px;height:138px;background:#fff;box-shadow:0 4px 10px rgba(0,0,0,.08)}
.card-body h3{font-family:"Noto Sans",sans-serif;font-size:16px;font-weight:700;color:var(--ink);margin:30px 0 0 22px}
.card-body p{font-size:12px;line-height:20px;color:var(--text);margin:8px 20px 0 20px}
.icon-disc{width:60px;height:60px;border-radius:50%;background:var(--red);display:flex;align-items:center;justify-content:center}

/* why */
.why{left:0;top:2095px;width:1200px;height:575px;background:linear-gradient(90deg,#b9a58e 0%,#8b8c95 30%,#2a3a70 55%,#14235d 100%)}
.feature{left:624px;width:444px;height:105px;background:rgba(44,62,120,.8);border-left:4px solid #d8d8e0}
.feature.active{border-left-color:var(--red)}
.feature h4{position:absolute;left:96px;top:24px;font-size:14px;font-weight:700;color:#fff}
.feature p{position:absolute;left:96px;top:46px;width:330px;font-size:12px;line-height:20px;color:#dfe3ef}
.feature svg{position:absolute;left:28px;top:30px}

/* testimonials */
.testimonials{left:0;top:2670px;width:1200px;height:610px;background:var(--light)}
.quote{width:304px;height:174px;background:#fff;padding:28px 22px;font-size:14px;line-height:23px;color:#555}
.quote.active{background:var(--red);color:#fff}
.tail{width:0;height:0;border-top:20px solid #fff;border-right:20px solid transparent}
.tail.active{border-top-color:var(--red)}
.avatar{width:54px;height:54px;border-radius:50%;background:linear-gradient(#a9b1bf,#59627a);border:3px solid #fff}
.person b{display:block;font-size:13px;color:var(--ink)}
.person span{font-size:12px;color:#aaa}

/* contact */
.touch-title{font-family:"Libre Baskerville",serif;font-size:42px;color:var(--ink)}
.contact-box{left:147px;top:3430px;width:908px;height:292px;background:#fff;box-shadow:0 2px 14px rgba(0,0,0,.1)}
.contact-side{left:147px;top:3430px;width:304px;height:292px;background:var(--grey)}
.field-label{font-size:13px;color:#333}
.field-line{height:1px;background:#999}
.row{display:flex;gap:10px;align-items:flex-start;font-size:13px;line-height:19px;color:#333}

/* footer */
.footer-box{top:4061px;width:271px;height:56px;border-top:6px solid #242c48;border-bottom:6px solid #242c48;display:flex;align-items:center;gap:12px;color:#fff}
.footer-nav a{position:absolute;font-size:12px;color:#fff;text-decoration:none}
.social{width:20px;height:20px;border-radius:50%;background:#fff}
</style>
</head>
<body>

<!-- header -->
<header class="abs site-header"></header>
<div class="abs brand"><span class="brand-mark"></span><span class="brand-name">TRL Vetting</span></div>

<div class="abs contact-item" style="left:414px">
  <svg width="36" height="36" viewBox="0 0 36 36"><rect x="7" y="7" width="22" height="22" transform="rotate(45 18 18)" fill="none" stroke="#2bb7a0" stroke-width="1.5"/><path d="M18 11a5 5 0 0 0-5 5c0 4 5 9 5 9s5-5 5-9a5 5 0 0 0-5-5z" fill="#2bb7a0"/><circle cx="18" cy="16" r="2" fill="#fff"/></svg>
  <div>Email Address<br>desk@trlvetting.example</div>
</div>
<div class="abs contact-item" style="left:659px">
  <svg width="36" height="36" viewBox="0 0 36 36"><rect x="7" y="7" width="22" height="22" transform="rotate(45 18 18)" fill="none" stroke="#2bb7a0" stroke-width="1.5"/><path d="M18 11a5 5 0 0 0-5 5c0 4 5 9 5 9s5-5 5-9a5 5 0 0 0-5-5z" fill="#2bb7a0"/><circle cx="18" cy="16" r="2" fill="#fff"/></svg>
  <div>Email Address<br>desk@trlvetting.example</div>
</div>
<div class="abs contact-item" style="left:905px">
  <svg width="36" height="36" viewBox="0 0 36 36"><rect x="7" y="7" width="22" height="22" transform="rotate(45 18 18)" fill="none" stroke="#2bb7a0" stroke-width="1.5"/><path d="M18 11a5 5 0 0 0-5 5c0 4 5 9 5 9s5-5 5-9a5 5 0 0 0-5-5z" fill="#2bb7a0"/><circle cx="18" cy="16" r="2" fill="#fff"/></svg>
  <div>Email Address<br>desk@trlvetting.example</div>
</div>

<nav class="abs nav">
  <a style="left:66px">Home</a><a style="left:157px">About Us</a><a style="left:258px">Services</a><a style="left:352px">FAQ</a><a style="left:433px">Contact Us</a>
</nav>
<div class="abs btn-appoint">Appointment</div>

<!-- hero -->
<div class="abs hero-photo" role="img" aria-label="Business team reviewing documents at a meeting table, tinted in navy blue"></div>
<div class="abs hero-box"></div>
<div class="abs hero-bar"></div>
<h1 class="abs hero-title">Insightful Checks for<br>Secure Choices</h1>
<p class="abs hero-text">It is a long and established fact that a reader will be distracted by the readable content of a page when looking.</p>
<div class="abs btn-red" style="left:118px;top:566px;width:197px;height:46px">REQUEST A DEMO</div>

<svg class="abs" style="left:0;top:780px" width="1200" height="280" viewBox="0 0 1200 280">
  <path d="M0 50 Q300 20 520 30 Q900 40 1200 170 L1200 280 L0 280 Z" fill="#fff"/>
  <path d="M470 30 Q900 30 1200 260 L1200 225 Q930 45 470 30 Z" fill="#c21d2e"/>
</svg>

<!-- about -->
<svg class="abs" style="left:0;top:1010px" width="480" height="422" viewBox="0 0 480 422">
  <defs><clipPath id="aboutClip"><circle cx="234" cy="213" r="209"/></clipPath></defs>
  <path d="M234 4 A209 209 0 0 1 420 330 L390 422 L400 422 Q460 300 420 150 Q370 30 234 4Z" fill="#c21d2e"/>
  <rect x="0" y="0" width="480" height="422" clip-path="url(#aboutClip)" fill="#3d5278" role="img" aria-label="Businessman in a suit working at a desk"/>
  <circle cx="421" cy="102" r="58" fill="#eef2f8"/>
</svg>

<div class="abs label" style="left:604px;top:992px">Who we are</div>
<h2 class="abs heading" style="left:604px;top:1024px;font-size:37px;line-height:46px">Ensuring Safety with<br>Every Verification</h2>
<h3 class="abs" style="left:604px;top:1143px;font-family:'Noto Sans',sans-serif;font-weight:400;font-size:19px;color:var(--navy)">The Key to Secure Decisions</h3>
<div class="abs about-text" style="left:604px;top:1183px;width:460px">
  <p>Lorem ipsum dolor sit amet, consectetur adipiscing elit, sed do eiusmod temp or incididunt ut labore et dolore magna aliqua. Ut enim ad minim veniam, quis laboris nisi ut aliquip ex ea commodo consequat.</p>
  <p style="margin-top:10px">Lorem ipsum dolor sit amet, consectetur adipiscing elit, sed do eiusmod temp or incididunt ut labore et dolore magna aliqua.</p>
</div>
<div class="abs btn-red" style="left:604px;top:1315px;width:136px;height:39px;font-size:13px">Contact us
  <svg width="16" height="12" viewBox="0 0 16 12"><path d="M1 6h13M9 1l5 5-5 5" stroke="#fff" stroke-width="1.5" fill="none"/></svg></div>

<!-- services -->
<section class="abs services"></section>
<div class="abs label" style="left:0;width:1200px;text-align:center;top:1522px">Our Services</div>
<h2 class="abs heading" style="left:0;width:1200px;text-align:center;top:1556px;font-size:42px">Services We <span style="color:var(--red)">Provide</span></h2>

<div class="abs card-photo" style="left:118px;top:1654px;background:linear-gradient(135deg,#cfd4da,#5a5f6b)" role="img" aria-label="Two colleagues in suits talking in an office"></div>
<div class="abs card-photo" style="left:447px;top:1654px;background:linear-gradient(135deg,#e4e4e4,#2a2a2e)" role="img" aria-label="Woman in a black top holding a tablet"></div>
<div class="abs card-photo" style="left:774px;top:1654px;background:linear-gradient(135deg,#c5cdd6,#3f4a5d)" role="img" aria-label="Colleagues looking at a laptop together"></div>

<div class="abs card-body" style="left:185px;top:1883px"><h3>County Criminal</h3><p>Lorem ipsum dolor sit amet, co nsectetur adipiscing elit, s</p></div>
<div class="abs card-body" style="left:514px;top:1883px"><h3>Public Records</h3><p>Lorem ipsum dolor sit amet, co nsectetur adipiscing elit, s</p></div>
<div class="abs card-body" style="left:841px;top:1883px"><h3>Employment Screen</h3><p>Lorem ipsum dolor sit amet, co nsectetur adipiscing elit, s</p></div>

<div class="abs icon-disc" style="left:155px;top:1852px"><svg width="28" height="28" viewBox="0 0 28 28" fill="none" stroke="#fff" stroke-width="1.5"><circle cx="14" cy="8" r="5"/><path d="M4 25c1-7 5-10 10-10s9 3 10 10z"/></svg></div>
<div class="abs icon-disc" style="left:484px;top:1852px"><svg width="28" height="28" viewBox="0 0 28 28" fill="none" stroke="#fff" stroke-width="1.5"><circle cx="14" cy="8" r="5"/><path d="M4 25c1-7 5-10 10-10s9 3 10 10z"/></svg></div>
<div class="abs icon-disc" style="left:811px;top:1852px"><svg width="28" height="28" viewBox="0 0 28 28" fill="none" stroke="#fff" stroke-width="1.5"><circle cx="14" cy="8" r="5"/><path d="M4 25c1-7 5-10 10-10s9 3 10 10z"/></svg></div>

<!-- why -->
<section class="abs why" role="img" aria-label="Group of professionals talking in a bright lobby, fading into navy"></section>
<div class="abs label" style="left:621px;top:2145px">Why choose us</div>
<h2 class="abs heading" style="left:621px;top:2176px;font-size:37px;line-height:47px;color:#fff">Confidence Starts with<br>a Clear Background</h2>

<div class="abs feature active" style="top:2287px">
  <svg width="40" height="40" viewBox="0 0 40 40" fill="none" stroke="#fff" stroke-width="1.5"><circle cx="20" cy="12" r="7"/><path d="M6 36c1-9 7-14 14-14s13 5 14 14z"/></svg>
  <h4>CLIENT-CENTRIC</h4><p>Lorem ipsum dolor sit amet, consectetur adipiscing elit, sed do eiusmod tempor incidid</p>
</div>
<div class="abs feature" style="top:2398px">
  <svg width="40" height="40" viewBox="0 0 40 40" fill="none" stroke="#fff" stroke-width="1.5"><path d="M20 4l15 11-6 18H11L5 15z"/></svg>
  <h4>PROFESSIONALISM</h4><p>Lorem ipsum dolor sit amet, consectetur adipiscing elit, sed do eiusmod tempor incidid</p>
</div>
<div class="abs feature" style="top:2510px">
  <svg width="40" height="40" viewBox="0 0 40 40" fill="none" stroke="#fff" stroke-width="1.5"><path d="M6 30a16 16 0 1 1 28 0"/><path d="M20 22l6-8"/><circle cx="20" cy="22" r="2"/></svg>
  <h4>EXPERIENCED EXPERTS</h4><p>Lorem ipsum dolor sit amet, consectetur adipiscing elit, sed do eiusmod tempor incidid</p>
</div>

<!-- testimonials -->
<section class="abs testimonials"></section>
<div class="abs label" style="left:0;width:1200px;text-align:center;top:2764px">Testimonials</div>
<h2 class="abs heading" style="left:0;width:1200px;text-align:center;top:2798px;font-size:42px">What Clients are <span style="color:var(--red)">Saying</span></h2>

<div class="abs quote" style="left:118px;top:2897px">Lorem ipsum dolor sit amet, consectetur adipiscing elit, sed d o eiusmod tempor incididunt ut lab ore et dolore magna aliqua. Ut enim ad min</div>
<div class="abs quote active" style="left:447px;top:2897px">Lorem ipsum dolor sit amet, consectetur adipiscing elit, sed d o eiusmod tempor incididunt ut lab ore et dolore magna aliqua. Ut enim ad min</div>
<div class="abs quote" style="left:776px;top:2897px">Lorem ipsum dolor sit amet, consectetur adipiscing elit, sed d o eiusmod tempor incididunt ut lab ore et dolore magna aliqua. Ut enim ad min</div>
<div class="abs tail" style="left:118px;top:3071px;border-top-color:var(--red)"></div>
<div class="abs tail active" style="left:447px;top:3071px"></div>
<div class="abs tail" style="left:776px;top:3071px;border-top-color:var(--red)"></div>

<div class="abs avatar" style="left:137px;top:3097px" role="img" aria-label="Client portrait"></div>
<div class="abs person" style="left:210px;top:3100px"><b>Dana Reyes</b><span>Engineer</span></div>
<div class="abs avatar" style="left:464px;top:3097px" role="img" aria-label="Client portrait"></div>
<div class="abs person" style="left:538px;top:3100px"><b>Dana Reyes</b><span>Engineer</span></div>
<div class="abs avatar" style="left:795px;top:3097px" role="img" aria-label="Client portrait"></div>
<div class="abs person" style="left:869px;top:3100px"><b>Dana Reyes</b><span>Engineer</span></div>

<svg class="abs" style="left:568px;top:3197px" width="64" height="12" viewBox="0 0 64 12">
  <rect x="2" y="2" width="20" height="8" rx="4" fill="#c21d2e"/><circle cx="32" cy="6" r="4" fill="#13225f"/><circle cx="44" cy="6" r="4" fill="#13225f"/><circle cx="56" cy="6" r="4" fill="#13225f"/>
</svg>

<!-- contact -->
<h2 class="abs touch-title" style="left:0;width:1200px;text-align:center;top:3330px">Get In <span style="color:var(--red)">Touch</span></h2>

<svg class="abs" style="left:0;top:3660px" width="1200" height="638" viewBox="0 0 1200 638">
  <path d="M0 0 Q120 170 420 240 Q600 265 760 260 L1200 260 L1200 638 L0 638 Z" fill="#0d1530"/>
  <path d="M0 0 Q90 160 420 240 Q580 265 740 258 Q480 262 300 212 Q80 150 0 60 Z" fill="#c21d2e"/>
  <path d="M0 60 Q80 150 300 212 Q420 245 560 255 Q380 258 260 230 Q70 185 0 110 Z" fill="#fff"/>
</svg>

<div class="abs contact-box"></div>
<div class="abs contact-side"></div>
<div class="abs" style="left:180px;top:3455px;font-family:'Libre Baskerville',serif;font-size:33px;color:#333">Address</div>
<div class="abs row" style="left:180px;top:3525px">
  <svg width="20" height="20" viewBox="0 0 20 20" fill="none" stroke="#c21d2e" stroke-width="1.4"><circle cx="10" cy="6" r="4"/><path d="M2 18c1-5 4-7 8-7s7 2 8 7z"/></svg>
  <div>Company Name<br>Suite 12 Elm Ave<br>City, Country</div>
</div>
<div class="abs row" style="left:180px;top:3600px;font-weight:600">
  <svg width="20" height="20" viewBox="0 0 20 20" fill="none" stroke="#c21d2e" stroke-width="1.4"><path d="M4 2l4 1 1 4-2 2a11 11 0 0 0 5 5l2-2 4 1 1 4-2 2C9 19 1 11 2 4z"/></svg>
  <div>555-010-2040 Or 555-010-3050</div>
</div>
<div class="abs row" style="left:180px;top:3640px">
  <svg width="20" height="20" viewBox="0 0 20 20" fill="none" stroke="#c21d2e" stroke-width="1.4"><rect x="2" y="3" width="16" height="14"/><path d="M2 3l8 8 8-8"/></svg>
  <div>hello@trlvetting.example</div>
</div>

<div class="abs field-label" style="left:471px;top:3472px">Name:</div>
<div class="abs field-line" style="left:471px;top:3497px;width:265px"></div>
<div class="abs field-line" style="left:771px;top:3497px;width:267px"></div>
<div class="abs field-label" style="left:471px;top:3518px">Phone:</div>
<div class="abs field-line" style="left:471px;top:3544px;width:265px"></div>
<div class="abs field-line" style="left:771px;top:3544px;width:267px"></div>
<div class="abs field-label" style="left:471px;top:3561px">Details:</div>
<div class="abs field-line" style="left:471px;top:3610px;width:564px"></div>
<div class="abs btn-red" style="left:472px;top:3643px;width:187px;height:37px;border-radius:19px;font-family:'Libre Baskerville',serif;font-weight:400;font-size:12px">QUICK ENQUIRY
  <svg width="14" height="10" viewBox="0 0 14 10"><path d="M1 5h11M8 1l4 4-4 4" stroke="#fff" stroke-width="1.4" fill="none"/></svg></div>

<!-- footer -->
<div class="abs footer-box" style="left:175px;padding-left:48px;font-size:12px;line-height:15px">
  <svg width="16" height="20" viewBox="0 0 16 20"><path d="M8 0a7 7 0 0 0-7 7c0 5 7 13 7 13s7-8 7-13a7 7 0 0 0-7-7z" fill="#c21d2e"/><circle cx="8" cy="7" r="2.5" fill="#0d1530"/></svg>
  <div>48 HARBOR LANE<br>COUNTRY</div>
</div>
<div class="abs" style="left:480px;top:4050px;width:240px;display:flex;align-items:center;justify-content:center;gap:10px">
  <span style="width:30px;height:30px;border-radius:50%;background:var(--red)"></span>
  <span style="font-family:'Noto Sans',sans-serif;font-weight:700;font-size:28px;color:#fff">TRL Vetting</span>
</div>
<div class="abs footer-box" style="left:761px;padding-left:48px;font-size:21px">
  <svg width="16" height="20" viewBox="0 0 16 20"><path d="M8 0a7 7 0 0 0-7 7c0 5 7 13 7 13s7-8 7-13a7 7 0 0 0-7-7z" fill="#c21d2e"/><circle cx="8" cy="7" r="2.5" fill="#0d1530"/></svg>
  <div>555 010 7788</div>
</div>
<div class="abs" style="left:0;width:1200px;text-align:center;top:4128px;font-size:12px;color:var(--red)">hello@trlvetting.example</div>
<div class="abs" style="left:538px;top:4159px;display:flex;gap:7px">
  <span class="social"></span><span class="social"></span><span class="social"></span><span class="social"></span><span class="social"></span>
</div>
<nav class="abs footer-nav" style="left:0;top:4212px;width:1200px;height:20px">
  <a style="left:278px">HOME</a><a style="left:353px">SERVICES</a><a style="left:453px">ABOUT US</a><a style="left:559px">PROJECTS</a><a style="left:659px">TESTIMONIALS</a><a style="left:797px">FAQ</a><a style="left:865px">CONTACT US</a>
</nav>

</body>
</html>
```